Crestwater Paving business card design

We need a business card developed for a local ready mix concrete company. We want a 2 sided design

The front just needs the basic contact info:

Douglas Venkatraman
P.555-214-6371
F. 555-214-6385
www.CrestwaterPaving.Com
Douglas@CrestwaterPaving.com
P.O Box 846
Millbrook, NJ, 07990

Service All of North And Central New Jersey With Ready Mix Concrete

The back will have a simple bullet point list:
• Metered Delivery - Use only what you pay for
• No Waste
• Multiple slumps on the fly
• No minimum delivery
• 24-7 service, all year
• No Hot Loads
• Fastest Service in the industry

I like the submissions using the existing colors. I think blue might also be a color to use as well. For the next trucks we order we will probably paint them blue. Colbalt blue

I must have made a typo: It should read, Serving all of North and Central New Jersey. It should also say: Pay for only what you use.

Target Market(s)

We will be targeting the construction industry

Industry/Entity Type

Concrete

Font styles to use
Serif
Sans Serif

Colors
ec2027

Requirements
Must have
• It needs to have a clean uncluttered look. The back is dedicated to telling customer what we do. Our advantage is we use a truck that delivers concrete with several advantages over barrel trucks, hence, why the back bullet points are important
Nice to have
• Our logo. I think since our logo is green, the front might look good with some red, like a red background (also the color of our truck)
Should not have
• clip art.

```html
<!DOCTYPE html>
<html lang="en">
<head>
<meta charset="utf-8">
<title>Crestwater Paving – Business Card</title>
<link rel="stylesheet" href="https://fonts.googleapis.com/css2?family=Open+Sans:ital,wght@0,400;0,600;0,800;1,400&display=swap">
<style>
  :root {
    --page: #e9e7e4;
    --card-white: #fbfbfb;
    --lime: #a6d20f;
    --blue: #1a86c8;
    --cobalt-dark: #1f3a8c;
    --cobalt-light: #3b5fc0;
    --graphite: #4a4a4c;
    --silver: #c9c9c9;
    --ink: #ffffff;
    --logo-ink: #2b2b2b;
  }
  * { box-sizing: border-box; margin: 0; padding: 0; }
  html, body { width: 832px; height: 1200px; overflow: hidden; }
  body {
    background: var(--page);
    font-family: "Open Sans", Arial, sans-serif;
    display: flex;
    flex-direction: column;
    align-items: center;
    justify-content: center;
    gap: 90px;
  }
  .card {
    width: 700px;
    height: 400px;
    position: relative;
    overflow: hidden;
    box-shadow: 0 6px 18px rgba(0,0,0,.18);
  }
  .vertical {
    writing-mode: vertical-rl;
    transform: rotate(180deg);
  }

  /* Front */
  .card--front { background: var(--card-white); }
  .front__brand {
    position: absolute;
    left: 30px; top: 34px;
    display: flex; align-items: center; gap: 10px;
    font-weight: 800; font-size: 26px; color: var(--logo-ink);
  }
  .front__brand-mark { width: 18px; height: 18px; background: var(--lime); }
  .front__bands {
    position: absolute;
    left: 210px; right: 30px; bottom: 0; top: 0;
    display: flex; align-items: flex-end; gap: 12px;
  }
  .band { height: 100%; display: flex; align-items: flex-start; justify-content: center; padding: 18px 0; color: var(--ink); }
  .band--graphite { background: var(--graphite); width: 86px; height: 62%; }
  .band--silver { background: var(--silver); width: 34px; height: 48%; }
  .band--name { background: var(--blue); width: 96px; height: 100%; }
  .band--lime { background: var(--lime); width: 74px; font-size: 15px; line-height: 1.35; }
  .band--lime.band--address { height: 92%; }
  .band--lime.band--phones { height: 84%; }
  .band--lime.band--web { height: 76%; }
  .contact-name { font-size: 24px; font-weight: 600; line-height: 1.2; }
  .contact-role { font-size: 16px; line-height: 1.3; }

  /* Back */
  .card--back {
    background: linear-gradient(135deg, var(--cobalt-light), var(--cobalt-dark));
    display: flex; gap: 12px; padding: 0 14px 0 24px;
  }
  .back__brand {
    width: 100px; display: flex; align-items: center; justify-content: center;
    font-weight: 800; font-size: 28px; color: var(--lime); white-space: nowrap;
  }
  .service {
    flex: 1; background: var(--lime); color: var(--ink);
    display: flex; align-items: center; justify-content: flex-start;
    padding: 16px 0; font-style: italic; font-size: 17px; white-space: nowrap;
  }
</style>
</head>
<body>

  <section class="card card--front" aria-label="Business card front">
    <div class="front__brand"><span class="front__brand-mark"></span>Crestwater Paving</div>
    <div class="front__bands">
      <div class="band band--graphite"></div>
      <div class="band band--silver"></div>
      <div class="band band--name vertical">
        <div>
          <p class="contact-name">Douglas Venkatraman</p>
          <p class="contact-role">manager</p>
        </div>
      </div>
      <div class="band band--lime band--address vertical">
        <div><p>P.O Box 846</p><p>Millbrook, NJ, 07990</p></div>
      </div>
      <div class="band band--lime band--phones vertical">
        <div><p>555-214-6371</p><p>555-214-6385</p></div>
      </div>
      <div class="band band--lime band--web vertical">
        <div><p>Douglas@CrestwaterPaving.com</p><p>www.CrestwaterPaving.Com</p></div>
      </div>
    </div>
  </section>

  <section class="card card--back" aria-label="Business card back">
    <div class="back__brand vertical">Crestwater Paving</div>
    <p class="service vertical">Metered Delivery - Use only what you pay for</p>
    <p class="service vertical">No Waste</p>
    <p class="service vertical">Multiple slumps on the fly</p>
    <p class="service vertical">No minimum delivery</p>
    <p class="service vertical">24-7 service, all year</p>
    <p class="service vertical">No Hot Loads</p>
    <p class="service vertical">Fastest Service in the industry</p>
  </section>

</body>
</html>
```